Marlow Filing Desk

We need one (1) unique homepage and five (5) interior pages. We will guarantee this project if the early submissions look promising.
Updates

Project Deadline Extended
Reason: We want to make sure that everyone who wants to submit a design has the time to do so, and to make revisions if necessary. Thanks.

Take a look at sites like http://www.quillnorth.com/, or http://brevo.com/ for some of the sleek, uncluttered design sensibilities we are looking for. Thanks.

Target Market(s)

Men and women who earn under $50,000 a year.

Industry/Entity Type

Interior

Requirements
Must have
• Logo prominently displayed
Tagline: "Affordable Expertise. Only $249."
Call to action button: "Order Now"
Five line, two column chart comparing us to our competitors
Live chat icon
Social media icons
Zentapay, Orla, QR, Ferro, Halvester, Pexbridge Till
Top-level navigation (home, our process, order now, contact, FAQ)
Login (email, password)
Nice to have
• Rotating flash banner for brief quotations or stock photos
Should not have
• We don't like a lot of busy images and colors. One bold color with a few accents here and there is what we prefer. Look to a site like www.tiltgrid.com, www.feltmundrow.com (mostly the landing page is what we like), www.pondlark.com and www.vunel.com.

```html
<!DOCTYPE html>
<html lang="en">
<head>
<meta charset="utf-8">
<title>Marlow Filing Desk</title>
<link href="https://fonts.googleapis.com/css2?family=Source+Sans+3:wght@400;600;700&display=swap" rel="stylesheet">
<style>
:root{
  --blue:#2b8ce3;
  --blue-mid:#5ea9ef;
  --blue-light:#9ccbf4;
  --ink:#333;
  --text:#666;
  --muted:#888;
  --band:#ececec;
  --white:#fff;
  --rule:#d8d8d8;
}
*{margin:0;padding:0;box-sizing:border-box}
html,body{width:1200px;height:916px;overflow:hidden;background:var(--white);font-family:"Source Sans 3",sans-serif;color:var(--text)}
.page{position:relative;width:1200px;height:916px}
.topbar{position:absolute;left:0;top:0;width:1200px;height:4px;background:var(--blue)}
.logo{position:absolute;left:166px;top:44px;display:flex;align-items:center;gap:12px}
.logo-square{width:40px;height:40px;background:var(--blue)}
.logo-name{font-size:38px;font-weight:600;color:var(--ink);letter-spacing:-.5px}
.client-login{position:absolute;left:842px;top:4px;width:82px;height:21px;background:#bdbdbd;color:var(--white);font-size:12px;text-align:center;line-height:21px;border-radius:0 0 3px 3px}
.live-chat{position:absolute;left:950px;top:11px;display:flex;align-items:center;gap:5px;color:var(--blue);font-size:13px;font-weight:600}
.nav{position:absolute;top:63px;left:0;font-size:12.5px;color:var(--text)}
.nav span{position:absolute;white-space:nowrap}
.hero{position:absolute;left:0;top:111px;width:1200px;height:387px;background:var(--band);border-top:1px solid #e0e0e0}
.hero-visual{position:absolute;left:194px;top:45px;width:365px;height:334px;border-radius:6px;background:linear-gradient(#3a3a3a 0%,#5c5c5c 70%,#f6f6f6 80%,#fff 100%)}
.headline{position:absolute;left:580px;top:40px;font-size:54px;font-weight:700;color:var(--blue);letter-spacing:-1px;line-height:1}
.price{position:absolute;left:580px;top:100px;width:446px;text-align:center;font-size:42px;font-weight:700;color:var(--blue);line-height:1}
.hero-copy{position:absolute;left:582px;top:153px;width:440px;font-size:12.5px;line-height:18px;color:var(--text)}
.order-btn{position:absolute;left:694px;top:222px;width:199px;height:54px;background:var(--blue);border-radius:6px;color:var(--white);font-size:28px;font-weight:700;text-align:center;line-height:54px;letter-spacing:.5px;box-shadow:0 2px 4px rgba(0,0,0,.2)}
.pay-label{position:absolute;left:696px;top:320px;width:200px;text-align:center;font-size:14px;color:var(--text)}
.pay{position:absolute;top:346px;width:54px;height:34px;background:var(--blue);border-radius:3px;color:var(--white);font-size:9.5px;font-weight:700;display:flex;align-items:center;justify-content:center;text-align:center;line-height:1}
.welcome h2,.chart h2{position:absolute;top:520px;font-size:21px;font-weight:600;color:var(--muted)}
.welcome h2 em,.chart h2 em{font-style:normal;color:var(--blue)}
.welcome-copy{position:absolute;left:164px;top:553px;width:360px;font-size:12.5px;line-height:18px}
.list-item{position:absolute;left:172px;width:310px;height:30px}
.list-item .mark{position:absolute;left:0;top:0;width:21px;height:26px;border:1px solid #ccc;background:#f6f6f6}
.list-item .txt{position:absolute;left:38px;top:3px;font-size:12.5px;white-space:nowrap}
.list-item .line{position:absolute;left:25px;top:24px;width:284px;height:2px;background:var(--rule)}
.divider{position:absolute;left:552px;top:507px;width:3px;height:321px;background:#ddd}
.cell{position:absolute;height:37px;color:var(--white);font-size:16px;display:flex;align-items:center;justify-content:center}
.cell.head{background:var(--blue)}
.cell.l{background:var(--blue-light)}
.cell.m{background:var(--blue-mid)}
.note{position:absolute;left:602px;top:810px;font-size:12px;color:var(--muted)}
.footer{position:absolute;left:0;top:839px;width:1200px;height:77px;background:var(--band);border-top:3px solid #dcdcdc}
.copyright{position:absolute;left:166px;top:40px;font-size:12.5px;color:var(--muted)}
.copyright em{font-style:normal;color:var(--blue)}
.social{position:absolute;top:32px;width:39px;height:38px;background:var(--blue);border-radius:3px;color:var(--white);font-size:10px;font-weight:700;display:flex;align-items:center;justify-content:center}
</style>
</head>
<body>
<div class="page">
  <div class="topbar"></div>
  <header>
    <div class="logo"><div class="logo-square"></div><div class="logo-name">Marlow Filing Desk</div></div>
    <div class="client-login">Client Login</div>
    <div class="live-chat">
      <svg width="20" height="16" viewBox="0 0 20 16"><path d="M10 1C5 1 1 3.8 1 7.2c0 2 1.3 3.7 3.4 4.8L3.5 15l4-2.4c.8.2 1.6.3 2.5.3 5 0 9-2.8 9-6.2S15 1 10 1z" fill="#2b8ce3"/></svg>
      Live Chat
    </div>
    <nav class="nav">
      <span style="left:585px">Home</span>
      <span style="left:652px">About Us</span>
      <span style="left:736px">Our Process</span>
      <span style="left:835px">Order Now</span>
      <span style="left:926px">Contact Us</span>
      <span style="left:1008px">FAQ</span>
    </nav>
  </header>

  <section class="hero">
    <div class="hero-visual" role="img" aria-label="Desktop monitor on a white stand showing a preview of the website"></div>
    <div class="headline">Affordable Expertise</div>
    <div class="price">@ Only $249</div>
    <p class="hero-copy">Lorem ipsum dolor sit amet, consectetur adipisicing elit, sed do eiusmod tempor incididunt ut labore et dolore magna aliqua. Ut enim ad minim veniam, quis officia deserunt mollit anim id est laborum.</p>
    <div class="order-btn">ORDER NOW</div>
    <div class="pay-label">Payment Option</div>
    <div class="pay" style="left:615px">Zentapay</div>
    <div class="pay" style="left:681px">Orla</div>
    <div class="pay" style="left:746px">QR</div>
    <div class="pay" style="left:812px">Halvester</div>
    <div class="pay" style="left:877px">Pexbridge Till</div>
    <div class="pay" style="left:941px">Ferro</div>
  </section>

  <section class="welcome">
    <h2 style="left:164px">Welcome to <em>MarlowFilingDesk</em></h2>
    <p class="welcome-copy">Lorem ipsum dolor sit amet, consectetur adipisicing elit, sed do eiusmod tempor incididunt ut labore et dolore magna aliqua. Ut enim ad minim veniam, quis&nbsp; officia deserunt mollit anim id est laborum.Lorem ipsum dolor sit amet, consectetur adipisicing elit, sed do eiusmod tempor.</p>
    <div class="list-item" style="top:654px"><div class="mark"></div><div class="txt">Lorem ipsum dolor sit amet, consectetur adipisi.</div><div class="line"></div></div>
    <div class="list-item" style="top:690px"><div class="mark"></div><div class="txt">Lorem ipsum dolor sit amet, consectetur adipisi.</div><div class="line"></div></div>
    <div class="list-item" style="top:726px"><div class="mark"></div><div class="txt">Lorem ipsum dolor sit amet, consectetur adipisi.</div><div class="line"></div></div>
    <div class="list-item" style="top:761px"><div class="mark"></div><div class="txt">Lorem ipsum dolor sit amet, consectetur adipisi.</div><div class="line"></div></div>
  </section>

  <div class="divider"></div>

  <section class="chart">
    <h2 style="left:581px">Comparision <em>Chart</em></h2>
    <div class="cell head" style="left:601px;top:555px;width:165px">Heading</div>
    <div class="cell head" style="left:771px;top:555px;width:122px">Heading - 01</div>
    <div class="cell head" style="left:897px;top:555px;width:122px">Heading - 02</div>

    <div class="cell head" style="left:601px;top:596px;width:165px">Heading</div>
    <div class="cell l" style="left:771px;top:596px;width:122px"><svg width="22" height="18"><path d="M2 10l6 6L20 2" stroke="#fff" stroke-width="4" fill="none"/></svg></div>
    <div class="cell l" style="left:897px;top:596px;width:122px">X</div>

    <div class="cell head" style="left:601px;top:637px;width:165px">Heading</div>
    <div class="cell m" style="left:771px;top:637px;width:122px"><svg width="22" height="18"><path d="M2 10l6 6L20 2" stroke="#fff" stroke-width="4" fill="none"/></svg></div>
    <div class="cell m" style="left:897px;top:637px;width:122px">X</div>

    <div class="cell head" style="left:601px;top:678px;width:165px">Heading</div>
    <div class="cell l" style="left:771px;top:678px;width:122px"><svg width="22" height="18"><path d="M2 10l6 6L20 2" stroke="#fff" stroke-width="4" fill="none"/></svg></div>
    <div class="cell l" style="left:897px;top:678px;width:122px"><svg width="22" height="18"><path d="M2 10l6 6L20 2" stroke="#fff" stroke-width="4" fill="none"/></svg></div>

    <div class="cell head" style="left:601px;top:719px;width:165px">Heading</div>
    <div class="cell m" style="left:771px;top:719px;width:122px"><svg width="22" height="18"><path d="M2 10l6 6L20 2" stroke="#fff" stroke-width="4" fill="none"/></svg></div>
    <div class="cell m" style="left:897px;top:719px;width:122px">X</div>

    <div class="cell head" style="left:601px;top:761px;width:165px">Heading</div>
    <div class="cell l" style="left:771px;top:761px;width:122px"><svg width="22" height="18"><path d="M2 10l6 6L20 2" stroke="#fff" stroke-width="4" fill="none"/></svg></div>
    <div class="cell l" style="left:897px;top:761px;width:122px"><svg width="22" height="18"><path d="M2 10l6 6L20 2" stroke="#fff" stroke-width="4" fill="none"/></svg></div>

    <div class="note">NOTE:&nbsp; Lorem ipsum dolor sit amet, consectetur adipisici.</div>
  </section>

  <footer class="footer">
    <div class="copyright">Copyright © 2011 |&nbsp; <em>Marlow Filing Desk</em></div>
    <div class="social" style="left:789px">Lynkt</div>
    <div class="social" style="left:837px">Fabo</div>
    <div class="social" style="left:885px">Tweel</div>
    <div class="social" style="left:934px">Vesk</div>
    <div class="social" style="left:983px">Feed</div>
  </footer>
</div>
</body>
</html>
```